Design a Hemp Museum + exhibition design**

I'm creating an Online Museum for Hemp which will tell the story of hemp from ancient times to now and the future
cover the medical, industrial and nutritional uses and development of hemp
the people behind it, researchers, politicians, farmers and influencerts

the museum will have a number of "wings" , each holds an exhibition around a differnet theme, for example:

Hemp in the Age of Empires: 18th and 19th Century Collections
Hemp - The History of Healing
Domestication and Early Use: Ancient Collection
From Cotton Gin to Plastics and Prohibition: Hemp's Decline

these are just a few sample ideas for exhibitions

I'm looking for an overall design for the museum home page and exhibition page which will make people curious and want to spend time,learning and browsing

Think mobile -first :)

You are requested to design

1. Home page
2. Exhibition page

Target Market(s)

Hemp aficionados, curious fans

Logo Text

The Lumen Museum

Coding

Coded - Design and coding required

Number of Pages Required

3 page

Font styles to use
Sans Serif
Decorative

Requirements
Must have
• a homepage design which prompts visitors to immediately start watching an exhibition

visitors need to understand that this is a museum , so that they dont think it's a business, a service provider or anything like that

needs to have the usual links to T&C, privacy, about us

needs to have a link to "Wander past the lantern stall"

must have a visual WOW effect
Nice to have
• animations, sounds etc
Should not have
• forms like contact us etc - not relevant

```html
<!DOCTYPE html>
<html lang="en">
<head>
<meta charset="utf-8">
<title>The Lumen Museum — Exhibitions</title>
<link href="https://fonts.googleapis.com/css2?family=Poppins:wght@400;500;600;700&display=swap" rel="stylesheet">
<style>
  :root {
    --ink: #050505;
    --card: #222222;
    --frame: #111111;
    --white: #ffffff;
    --orange: #f7941d;
    --green: #2bd12b;
    --red: #d91f1f;
    --yellow: #f2c31b;
    --wood-dark: #2a1d16;
    --wood-mid: #4a372c;
    --leaf: #4f9a2c;
    --leaf-light: #8fd157;
  }
  * { box-sizing: border-box; margin: 0; padding: 0; }
  html, body { width: 1200px; height: 800px; overflow: hidden; background: var(--ink); }
  body { font-family: "Poppins", sans-serif; color: var(--white); }

  .page {
    position: relative; width: 1200px; height: 800px; overflow: hidden;
    background:
      radial-gradient(ellipse 420px 260px at 600px 140px, rgba(120,120,120,.35), transparent 70%),
      radial-gradient(ellipse 300px 200px at 250px 420px, rgba(90,90,90,.25), transparent 70%),
      radial-gradient(ellipse 300px 220px at 950px 380px, rgba(90,90,90,.22), transparent 70%),
      var(--ink);
  }
  .table-top {
    position: absolute; left: 0; right: 0; bottom: 0; height: 180px;
    background: linear-gradient(180deg, rgba(0,0,0,0) 0%, var(--wood-mid) 35%, var(--wood-dark) 100%);
  }
  .foliage { position: absolute; }
  .foliage--right {
    right: 0; top: 100px; width: 190px; height: 680px;
    background: radial-gradient(ellipse at 80% 50%, var(--leaf-light) 0%, var(--leaf) 40%, rgba(79,154,44,0) 72%);
    opacity: .75;
  }
  .foliage--left {
    left: 0; bottom: 0; width: 170px; height: 210px;
    background: radial-gradient(ellipse at 30% 70%, var(--leaf-light) 0%, var(--leaf) 40%, rgba(79,154,44,0) 72%);
    opacity: .75;
  }
  .foliage--center {
    left: 490px; bottom: 0; width: 300px; height: 110px;
    background: radial-gradient(ellipse at 50% 70%, var(--leaf-light) 0%, var(--leaf) 40%, rgba(79,154,44,0) 72%);
    opacity: .8;
  }

  .site-header { position: absolute; top: 0; left: 0; right: 0; height: 104px; }
  .brand {
    position: absolute; left: 66px; top: 34px;
    font-size: 28px; font-weight: 700; letter-spacing: .2px; color: var(--white);
  }
  .nav-exhibitions {
    position: absolute; left: 862px; top: 38px; display: flex; align-items: center; gap: 10px;
    font-size: 14px; font-weight: 600; letter-spacing: .3px;
  }
  .nav-menu {
    position: absolute; left: 1033px; top: 27px; display: flex; align-items: center; gap: 10px;
    font-size: 14px; font-weight: 600; letter-spacing: .3px;
  }
  .menu-button {
    width: 51px; height: 51px; border-radius: 50%; background: var(--white);
    display: flex; align-items: center; justify-content: center;
  }

  .hero-title { position: absolute; top: 156px; left: 0; right: 0; text-align: center; }
  .hero-kicker { font-size: 27px; font-weight: 600; letter-spacing: .5px; line-height: 1; }
  .hero-headline { margin-top: 12px; font-size: 68px; font-weight: 700; letter-spacing: 1.5px; line-height: 1; }
  .hero-headline .accent { color: var(--orange); }

  .pager { position: absolute; left: 48px; top: 316px; font-size: 13px; font-weight: 700; }
  .pager li { list-style: none; line-height: 25px; }
  .pager .current::after {
    content: ""; display: block; width: 2px; height: 50px; background: #777; margin: 4px 0 6px 9px;
  }

  .exhibit-list { position: absolute; top: 302px; left: 102px; display: flex; gap: 11px; }
  .exhibit-card {
    width: 249px; height: 390px; background: var(--card);
    border-top: 2px solid var(--accent); padding: 24px 24px 0;
  }
  .exhibit-card--orange { --accent: var(--orange); }
  .exhibit-card--green { --accent: var(--green); }
  .exhibit-card--red { --accent: var(--red); }
  .exhibit-card--yellow { --accent: var(--yellow); }
  .exhibit-frame { width: 202px; height: 207px; background: var(--frame); padding: 7px; }
  .exhibit-image { width: 100%; height: 100%; }
  .exhibit-image--revolution { background: linear-gradient(135deg, #5f8a4a, #e8dcc8 55%, #8a3a2a); }
  .exhibit-image--healing { background: linear-gradient(160deg, #8c8c80, #a9a56a 50%, #3d4a22); }
  .exhibit-image--ancient { background: linear-gradient(180deg, #b7c6d6, #d8cdb2 45%, #7a5a3a); }
  .exhibit-image--decline { background: linear-gradient(135deg, #6a6a10, #c9c63a 45%, #2b3a12); }
  .exhibit-label {
    margin-top: 31px; font-size: 12px; font-weight: 700; letter-spacing: .2px; color: var(--accent);
  }
  .exhibit-title { margin-top: 8px; font-size: 16.5px; font-weight: 500; line-height: 24px; }
</style>
</head>
<body>
<main class="page">
  <div class="table-top"></div>
  <div class="foliage foliage--right" role="img" aria-label="Leafy green plant fronds along the right edge"></div>
  <div class="foliage foliage--left" role="img" aria-label="Green plant fronds in the lower left corner"></div>
  <div class="foliage foliage--center" role="img" aria-label="Green plant sprig on the table below the cards"></div>

  <header class="site-header">
    <div class="brand">The Lumen Museum</div>
    <a class="nav-exhibitions">
      <svg width="40" height="38" viewBox="0 0 40 38" fill="none" stroke="#fff" stroke-width="1.6">
        <rect x="3" y="6" width="34" height="22"/>
        <rect x="12" y="11" width="16" height="12"/>
        <path d="M3 6 L0 2 M37 6 L40 2 M20 28 V34 M12 36 H28 M3 28 V36 M37 28 V36"/>
      </svg>
      EXHIBITIONS
    </a>
    <a class="nav-menu">
      <span class="menu-button">
        <svg width="26" height="20" viewBox="0 0 26 20" stroke="#111" stroke-width="3" stroke-linecap="round">
          <path d="M8 2 H24 M2 10 H24 M8 18 H24"/>
        </svg>
      </span>
      MENU
    </a>
  </header>

  <section class="hero-title">
    <p class="hero-kicker">THE WORLD’S ONLY</p>
    <h1 class="hero-headline"><span class="accent">HEMP</span> EXHIBITION</h1>
  </section>

  <ol class="pager">
    <li class="current">01</li>
    <li>02</li>
    <li>03</li>
    <li>04</li>
    <li>05</li>
  </ol>

  <section class="exhibit-list">
    <article class="exhibit-card exhibit-card--orange">
      <div class="exhibit-frame"><div class="exhibit-image exhibit-image--revolution" role="img" aria-label="Painting of a fife and drum march with a flag"></div></div>
      <p class="exhibit-label">EXHIBITION</p>
      <h2 class="exhibit-title">Hemp in the Age of Empires: 18th and 19th Century Collections</h2>
    </article>
    <article class="exhibit-card exhibit-card--green">
      <div class="exhibit-frame"><div class="exhibit-image exhibit-image--healing" role="img" aria-label="Photo of a grower tending flowering plants"></div></div>
      <p class="exhibit-label">EXHIBITION</p>
      <h2 class="exhibit-title">Hemp<br>The History of<br>Healing</h2>
    </article>
    <article class="exhibit-card exhibit-card--red">
      <div class="exhibit-frame"><div class="exhibit-image exhibit-image--ancient" role="img" aria-label="Illustration of an ancient walled city with a procession"></div></div>
      <p class="exhibit-label">EXHIBITION</p>
      <h2 class="exhibit-title">Domestication and Early Use: Ancient Collection</h2>
    </article>
    <article class="exhibit-card exhibit-card--yellow">
      <div class="exhibit-frame"><div class="exhibit-image exhibit-image--decline" role="img" aria-label="Photo of plants growing under yellow indoor lights"></div></div>
      <p class="exhibit-label">EXHIBITION</p>
      <h2 class="exhibit-title">From Cotton Gin to Plastics &amp; Prohibition: Hemp's Decline</h2>
    </article>
  </section>
</main>
</body>
</html>
```